Shiftwell Hub

Our product is a subscription-based website for doctors and medical practices. It allows contract-based doctors (locums) to book jobs with medical practices and to organise their own finances (invoicing, pension, etc). Also, it allows medical practices to post jobs, and book locums.

We need a website design that looks clean and professional. It should look easy-to-use and friendly, which will encourage users to sign up as they'll hopefully think using the system will also be simple and friendly.

As well as the homepage, we need a design for the logged-in view. This is very different to the website but equally important. It needs to be very functional. Much more like an application and less like a website.

PLEASE SUBMIT BOTH WEBSITE HOMEPAGE DESIGN AND APPLICATION DASHBOARD DESIGN.

The application is built and we already have a user interface (linked below) so we're not looking for a designer to decide what is on these pages - we already have that. We're ONLY asking for visual design. Please just make the content we have look good. You may move parts of the content around a small amount but the functionality is very much signed off now so it's only visual styling that we need addressed.

Please base the branding around the current logo, which can't be changed. You can get the logo as an EPS here : http://clients.brambleotter.co.uk/shiftwellhub/design/logo-green.eps

Here is a link to the current design for the website, and for the application dashboard:
http://clients.brambleotter.co.uk/shiftwellhub/design/

Also, here is a video we've had made which might help you with the brand:
http://clipvaultnet.com/83051726

Just in case it isn't clear, the video (linked in the main brief) is an essential part of the website homepage.

Reason: We need to spend some time looking over these designs and might ask for a few amendments to one or two in the next few days. Thanks.

Target Market(s)

Doctors and medical practices

Industry/Entity Type

Medical

Requirements
Must have
• It must have all the features that are in the linked designs - homepage and dashboard.

```html
<!DOCTYPE html>
<html lang="en">
<head>
<meta charset="utf-8">
<title>Shiftwell Hub – Home</title>
<link href="https://fonts.googleapis.com/css2?family=Open+Sans:wght@400;600;700&family=Exo:wght@500;600&family=Droid+Serif:wght@700&display=swap" rel="stylesheet">
<style>
:root{
  --blue:#0f8ec9;
  --blue-dark:#0a76ad;
  --green:#6f9a1c;
  --green-dark:#5b8213;
  --text:#444;
  --muted:#666;
  --line:#d6d6d6;
  --white:#fff;
}
*{box-sizing:border-box;margin:0;padding:0}
html,body{width:754px;height:1200px;overflow:hidden}
body{position:relative;font-family:"Open Sans",Arial,sans-serif;color:var(--text);background:var(--white)}
.abs{position:absolute}
.header{left:4px;top:0;width:746px;height:96px;background:linear-gradient(#f4f4f4,#dedede);border-bottom:2px solid #c8c8c8}
.brand{left:80px;top:14px;display:flex;align-items:center;gap:10px}
.brand-dot{width:52px;height:52px;border-radius:50%;background:var(--blue)}
.brand-name{font-size:26px;font-weight:700;color:var(--blue);line-height:1}
.brand-tag{font-size:10px;color:var(--blue);margin-top:4px}
.user-name{left:578px;top:25px;font-size:12px;font-weight:600;color:var(--green)}
.btn{display:flex;align-items:center;justify-content:center;color:#fff;font-size:11px;font-weight:600;border-radius:4px}
.btn-green{background:linear-gradient(#85b22a,var(--green-dark))}
.btn-blue{background:linear-gradient(#2aa6e0,var(--blue-dark))}
.nav{left:0;top:110px;width:754px;height:33px;background:linear-gradient(#7ea926,var(--green-dark));display:flex;align-items:center;padding-left:78px;color:#fff;font-size:11.5px}
.nav span{margin:0 7px}
.nav .sep{margin:0 2px}
.nav .active{background:#fff;color:var(--green);padding:1px 8px;border-radius:2px;margin-left:0}
.video{left:84px;top:162px;width:309px;height:195px;border:1px solid #ccc}
.video-media{position:absolute;left:0;top:0;width:100%;height:171px;background:linear-gradient(#e6eef2,#cfdbe2)}
.video-bar{position:absolute;left:0;top:171px;width:100%;height:22px;background:linear-gradient(#eee,#cfcfcf);font-size:6px;color:#666}
.hero-title{left:418px;top:166px;font-family:"Exo",sans-serif;font-weight:600;font-size:18px;line-height:24px;color:#333;letter-spacing:1px}
.hero-title b{color:var(--blue);font-weight:600}
.benefits{left:417px;top:225px;list-style:none;font-size:11.5px;font-weight:600;color:#555}
.benefits li{display:flex;align-items:center;gap:6px;height:19px}
.plus{width:9px;height:9px;border-radius:50%;border:1px solid var(--green);position:relative}
.plus:before,.plus:after{content:"";position:absolute;background:var(--green)}
.plus:before{left:1px;top:3px;width:5px;height:1px}
.plus:after{left:3px;top:1px;width:1px;height:5px}
.band{left:0;top:374px;width:754px;height:288px;background:var(--blue);border-top:2px solid #0b7fb6;border-bottom:2px solid #fff;box-shadow:0 2px 0 var(--blue)}
.card{top:391px;width:294px;height:254px;background:#fff;border-radius:5px}
.card-tab{position:absolute;left:0;top:9px;height:26px;padding:0 22px 0 17px;color:#fff;font-weight:700;font-size:14px;display:flex;align-items:center;clip-path:polygon(0 0,88% 0,100% 50%,88% 100%,0 100%)}
.card-lead{position:absolute;left:16px;top:43px;font-size:10px}
.step{position:absolute;left:5px;width:280px}
.step h3{font-size:11px;font-weight:700;color:#555;display:flex;align-items:center;gap:3px}
.num{width:9px;height:9px;border:1px solid #666;border-radius:50%;font-size:6px;display:inline-flex;align-items:center;justify-content:center;font-weight:400}
.step p{font-size:8.8px;color:#555;padding-left:15px;margin-top:5px;line-height:12px}
.card-more{position:absolute;left:21px;top:222px;font-size:9.2px}
.strip{left:80px;top:676px;width:592px;height:39px;background:var(--green);border-radius:4px;display:flex;align-items:center;color:#fff;font-size:12px;padding-left:17px}
.strip .n{width:15px;height:15px;border-radius:50%;background:#fff;color:var(--green);font-size:10px;font-weight:700;display:inline-flex;align-items:center;justify-content:center;margin-right:6px}
.signup{left:76px;top:724px;width:601px;height:208px;border:1px solid var(--line);border-radius:4px;overflow:hidden}
.signup h2{position:absolute;left:10px;top:17px;font-size:13.5px;font-weight:400;color:#444}
.roles{position:absolute;left:11px;top:48px;font-size:9.5px;display:flex;gap:14px;align-items:center}
.radio{display:inline-block;width:9px;height:9px;border:2px solid var(--green);border-radius:50%;vertical-align:-1px;margin-right:2px}
.field{position:absolute;font-size:10.5px;color:#555}
.field i{display:block;width:138px;height:23px;border:1px solid #bbb;border-radius:3px;margin-top:3px}
.agree{position:absolute;left:10px;top:170px;font-size:10.5px;display:flex;align-items:center;gap:5px}
.box{width:8px;height:8px;border:2px solid var(--green);background:#d8e9b8}
.nurse{position:absolute;right:0;top:70px;width:230px;height:138px;background:radial-gradient(circle at 60% 45%,#54b7d9,#cfe8ef 70%)}
.press{top:953px;width:184px;height:39px;border:1px solid #bbb;display:flex;align-items:center;justify-content:center;font-family:"Droid Serif",serif;font-weight:700;font-size:18px;color:#1c2e4a;white-space:nowrap}
.quotes{left:0;top:1000px;width:754px;height:92px;background:radial-gradient(circle at 50% 40%,#4ab4e2,var(--blue) 60%);border-top:3px solid var(--green)}
.quote{position:absolute;top:25px;width:240px;text-align:center;color:#fff;font-size:11px;font-weight:600;line-height:13.5px;letter-spacing:.3px}
.fnav{left:0;top:1092px;width:754px;height:36px;background:var(--green);display:flex;justify-content:center;align-items:center;gap:12px;color:#fff;font-size:11px;font-weight:600}
.footer{left:0;top:1128px;width:754px;height:56px;background:var(--blue);color:#fff;text-align:center;font-size:11px;font-weight:600;letter-spacing:.4px;line-height:14px;padding-top:4px}
.legal{left:0;top:1186px;width:754px;text-align:center;font-size:7px;color:#555}
</style>
</head>
<body>
<header class="abs header"></header>
<div class="abs brand">
  <div class="brand-dot"></div>
  <div>
    <div class="brand-name">Shiftwell Hub</div>
    <div class="brand-tag">Ger Connected. Stay organised.</div>
  </div>
</div>
<div class="abs user-name">Mrs. Helen Marsh</div>
<div class="abs btn btn-green" style="left:575px;top:45px;width:51px;height:26px">Sign out</div>
<div class="abs btn btn-blue" style="left:632px;top:45px;width:101px;height:26px">Go to Dashboard</div>

<nav class="abs nav">
  <span class="active">Home</span><span class="sep">|</span><span>Locums</span><span class="sep">|</span><span>Employers</span><span class="sep">|</span><span>Pricing</span><span class="sep">|</span><span>About us</span><span class="sep">|</span><span>FAQ</span><span class="sep">|</span><span>Contact us</span>
</nav>

<div class="abs video">
  <div class="video-media" role="img" aria-label="Video still of four smiling doctors in white coats">
    <svg width="48" height="48" style="position:absolute;left:130px;top:62px" viewBox="0 0 48 48"><circle cx="24" cy="24" r="21" fill="#fff" stroke="#1b93c8" stroke-width="4"/><path d="M19 15 L33 24 L19 33Z" fill="#777"/></svg>
  </div>
  <div class="video-bar">
    <svg width="309" height="22">
      <rect x="10" y="6" width="2" height="9" fill="#888"/><rect x="14" y="6" width="2" height="9" fill="#888"/>
      <rect x="27" y="8" width="148" height="5" rx="2.5" fill="#555"/><rect x="27" y="8" width="95" height="5" rx="2.5" fill="#888"/>
      <circle cx="91" cy="10.5" r="5" fill="#1b93c8" stroke="#fff"/>
      <text x="181" y="13" font-size="6" fill="#555">00:21 / 03:34</text>
      <rect x="232" y="6" width="3" height="9" fill="#1b93c8"/><rect x="237" y="6" width="3" height="9" fill="#1b93c8"/><rect x="242" y="6" width="3" height="9" fill="#888"/>
      <rect x="256" y="6" width="20" height="9" rx="2" fill="#ccc"/><text x="259" y="13" font-size="6" fill="#555">480p</text>
      <rect x="283" y="6" width="9" height="9" fill="none" stroke="#999"/>
    </svg>
  </div>
</div>

<h1 class="abs hero-title">A Network for connecting<br><b>Locums</b> with employers</h1>
<ul class="abs benefits">
  <li><span class="plus"></span>Better connectivity</li>
  <li><span class="plus"></span>More choice</li>
  <li><span class="plus"></span>Less paperwork</li>
  <li><span class="plus"></span>Lower costs</li>
</ul>
<div class="abs btn btn-blue" style="left:418px;top:321px;width:170px;height:26px;font-size:12px">Sign up for free-try us out</div>

<section class="abs band"></section>

<article class="abs card" style="left:80px">
  <div class="card-tab" style="background:var(--blue)">GP Locums</div>
  <div class="card-lead" style="color:var(--blue)">The complete platform to organise your locum life</div>
  <div class="step" style="top:66px"><h3><span class="num">1</span>Find Jobs</h3><p>Search, apply and get invited for a wide selection of jobs from practices and agencies</p></div>
  <div class="step" style="top:116px"><h3><span class="num">2</span>Do your locum admin easily online</h3><p>Profile, diary management, invoicing, pension forms, finances, tax returns</p></div>
  <div class="step" style="top:167px"><h3><span class="num">3</span>Create and grow your “Employer Network”</h3><p>Create your online profile and connect with your own network of employers allowing you to automatically fill jobs</p></div>
  <div class="card-more" style="color:var(--blue)">More about Shiftwell Hub for locums</div>
  <div class="btn btn-blue" style="position:absolute;left:223px;top:218px;width:64px;height:22px;border-radius:2px;font-weight:400">Sign Up</div>
</article>

<article class="abs card" style="left:380px">
  <div class="card-tab" style="background:var(--green)">Employers</div>
  <div class="card-lead" style="color:var(--green)">The complete platform to organise your locum life</div>
  <div class="step" style="top:66px"><h3><span class="num">1</span>Find locums</h3><p>Post your locumm requirements. Search and employ the right locums via your e-book system</p></div>
  <div class="step" style="top:116px"><h3><span class="num">2</span>Do your locum admin easily online</h3><p>Profile, diary management, pre-employment checks, locum market statistics</p></div>
  <div class="step" style="top:167px"><h3><span class="num">3</span>Create and grow your “employer network”</h3><p>Create your online profile and connect with your own network of locums allowing them to automatically fill jobs</p></div>
  <div class="card-more" style="color:var(--green-dark);left:19px">More about Shiftwell Hub for employers</div>
  <div class="btn btn-green" style="position:absolute;left:221px;top:218px;width:64px;height:22px;border-radius:2px;font-weight:400">Sign Up</div>
</article>

<div class="abs strip">
  <span class="n">1</span><span style="margin-right:36px">"The network" for Locums and employers</span>
  <span class="n">2</span><span style="margin-right:21px">Save time and Cost</span>
  <span class="n">3</span><span>Try it free now</span>
</div>

<section class="abs signup">
  <h2>Try it now with just an email address, GMC number and password!</h2>
  <div class="roles"><span>I am</span><span><span class="radio"></span>a Locum</span><span><span class="radio"></span>an employer</span></div>
  <label class="field" style="left:10px;top:77px">Email<i></i></label>
  <label class="field" style="left:173px;top:77px">GMC number<i></i></label>
  <label class="field" style="left:10px;top:120px">Password:<i></i></label>
  <label class="field" style="left:173px;top:120px">Confirm password:<i></i></label>
  <div class="agree"><span class="box"></span>I agree to the terms of service and the privacy policy</div>
  <div class="nurse" role="img" aria-label="Photo of a smiling nurse in blue scrubs writing on a clipboard"></div>
</section>

<div class="abs press" style="left:79px;color:#1c3a6e">dailyledger.co.uk</div>
<div class="abs press" style="left:284px;font-family:'Open Sans',sans-serif;font-weight:600">NewsPost</div>
<div class="abs press" style="left:490px">Northgate Herald</div>

<section class="abs quotes">
  <p class="quote" style="left:70px;top:23px">So easy to set up.Five minutes and you’re in.And it does all the boring admin stuff that i hate.<br>Name of person,Locum</p>
  <p class="quote" style="left:446px;top:23px">As a Practise, it’s great to be able to find Locums quickly and easily.No more time-consuming agency phone calls!<br>Blah Medical Centre</p>
</section>

<nav class="abs fnav"><span>Home</span><span>Locums</span><span>Employers</span><span>About us</span><span>FAQ</span><span>Contact us</span></nav>

<footer class="abs footer">
  <div style="margin-bottom:5px">We’re here to help : support@shiftwellhub.co.uk</div>
  <div>Copyright © 2013 Shiftwell Hub Ltd. All Rights Reserved</div>
  <div>Registered in England no.08214597</div>
</footer>
<div class="abs legal">Terms of service &nbsp;&nbsp;&nbsp;&nbsp;|&nbsp;&nbsp;&nbsp;&nbsp; Privacy policy &nbsp;&nbsp;&nbsp;&nbsp;|&nbsp;&nbsp;&nbsp;&nbsp; Refund policy</div>
</body>
</html>
```